Business Card Design for Property Development Company Director

I am looking for a professional and unforgettable business card design for our Director of our Property Development Company.
Please see attached .pptx file to find out what information to include. You don't have to follow the exact format shown in the file - I am interested to see your creative flair using the information provided.

```html
<!DOCTYPE html>
<html lang="en">
<head>
<meta charset="utf-8">
<title>Kestral Property Group – Business Card</title>
<link href="https://fonts.googleapis.com/css2?family=Arimo:wght@400;700&family=Lato:wght@400;700;900&family=Open+Sans:wght@700&display=swap" rel="stylesheet">
<style>
  :root {
    --page: #ffffff;
    --brand-blue: #1d4f9e;
    --name-blue: #1c3a8a;
    --blue-light: #4a7ad4;
    --blue-deep: #1a4593;
    --ink: #1a1a1a;
    --black: #111111;
    --grey-mark: #5a5a5a;
    --stripe-grey: #9b9b9b;
    --panel: #f3f3f3;
    --faint: #ececec;
    --icon-ring: #c9d6ee;
    --white: #ffffff;
  }
  * { margin: 0; padding: 0; box-sizing: border-box; }
  html, body { width: 960px; height: 1200px; overflow: hidden; background: var(--page); }
  .sheet { position: relative; width: 960px; height: 1200px; }

  .card {
    position: absolute; left: 80px; width: 800px; height: 480px; overflow: hidden;
    box-shadow: 8px 10px 6px rgba(0,0,0,0.28);
  }
  .card--front { top: 80px; background: var(--white); font-family: "Arimo", Arial, sans-serif; }
  .card--back { top: 640px; background: linear-gradient(180deg, var(--blue-light) 0%, var(--blue-deep) 100%); font-family: "Lato", Arial, sans-serif; }

  /* front */
  .front-texture {
    position: absolute; left: 400px; top: 0; width: 400px; height: 400px;
    background: radial-gradient(ellipse at 70% 60%, #ebebeb 0%, var(--panel) 55%, #f7f7f7 100%);
  }
  .front-ghost { position: absolute; left: 0; top: 50px; width: 300px; height: 300px; background: var(--faint); opacity: 0.8; }
  .front-shapes { position: absolute; inset: 0; width: 800px; height: 480px; }

  .brand { position: absolute; display: flex; align-items: center; gap: 14px; }
  .brand__square { width: 72px; height: 72px; flex: none; }
  .brand__name { font-family: "Arimo", Arial, sans-serif; font-weight: 700; line-height: 1; }
  .brand__word { display: block; }
  .brand__sub { display: block; }

  .brand--front { left: 66px; top: 170px; }
  .brand--front .brand__square { background: var(--grey-mark); }
  .brand--front .brand__name { color: var(--brand-blue); }
  .brand--front .brand__word { font-size: 44px; letter-spacing: 0.5px; }
  .brand--front .brand__sub { font-size: 16px; letter-spacing: 3.6px; margin-top: 6px; }

  .person { position: absolute; left: 463px; top: 104px; }
  .person__name { font-size: 33px; font-weight: 700; color: var(--name-blue); line-height: 1; }
  .person__role { font-size: 28px; font-weight: 400; color: var(--ink); line-height: 1; }

  .contacts { position: absolute; left: 463px; top: 188px; list-style: none; }
  .contact { display: flex; align-items: center; height: 30px; margin-bottom: 15px; color: var(--ink); }
  .contact svg { width: 28px; height: 28px; flex: none; margin-right: 18px; }
  .contact--phone { font-size: 18px; }
  .contact--mail { font-size: 17px; }
  .contact--web { font-size: 22px; }

  .licence { position: absolute; right: 20px; top: 434px; color: var(--white); font-size: 14px; font-weight: 700; }

  /* back */
  .tagline {
    position: absolute; top: 58px; width: 100%; text-align: center;
    font-family: "Open Sans", Arial, sans-serif; font-weight: 700; font-size: 16px; letter-spacing: 2.6px;
    color: #e8eefa;
  }
  .brand--back { left: 0; right: 0; top: 186px; justify-content: center; gap: 18px; }
  .brand--back .brand__square { width: 96px; height: 96px; background: var(--white); }
  .brand--back .brand__name { color: var(--white); }
  .brand--back .brand__word { font-size: 58px; letter-spacing: 0.5px; }
  .brand--back .brand__sub { font-size: 21px; letter-spacing: 4.4px; margin-top: 8px; }

  .offer-band {
    position: absolute; left: 0; bottom: 0; width: 100%; height: 82px; background: var(--black);
    display: flex; align-items: center; justify-content: center;
    color: var(--white); font-size: 18px; font-weight: 700; letter-spacing: -0.2px;
  }
  .offer-band strong { font-weight: 900; }
</style>
</head>
<body>
<main class="sheet">

  <section class="card card--front" aria-label="Business card front">
    <div class="front-ghost"></div>
    <div class="front-texture" role="img" aria-label="Soft light grey geometric texture"></div>

    <svg class="front-shapes" viewBox="0 0 536 322" preserveAspectRatio="none" aria-hidden="true">
      <polygon points="0,216 80,260 312,260 358,322 0,322" fill="#9b9b9b"/>
      <polygon points="0,226 78,270 304,270 346,322 0,322" fill="#111111"/>
      <polygon points="322,267 536,267 536,322 362,322" fill="#1d4f9e"/>
    </svg>

    <div class="brand brand--front">
      <span class="brand__square"></span>
      <span class="brand__name">
        <span class="brand__word">KESTRAL</span>
        <span class="brand__sub">PROPERTY GROUP</span>
      </span>
    </div>

    <div class="person">
      <p class="person__name">Daniel Marsh</p>
      <p class="person__role">Director</p>
    </div>

    <ul class="contacts">
      <li class="contact contact--phone">
        <svg viewBox="0 0 28 28" aria-hidden="true"><circle cx="14" cy="14" r="12.5" fill="#fff" stroke="#c9d6ee" stroke-width="1.5"/><path d="M10.2 8.2c.6-.5 1.3-.4 1.7.2l1.2 1.8c.3.5.2 1.1-.2 1.5l-.8.7c.6 1.4 1.6 2.5 3 3.2l.7-.8c.4-.4 1-.5 1.5-.2l1.8 1.1c.6.4.7 1.2.2 1.7l-.8.9c-.6.6-1.5.8-2.3.5-3.4-1.3-6-3.9-7.2-7.3-.3-.8-.1-1.7.5-2.3z" fill="#1d4f9e"/></svg>
        0491570156
      </li>
      <li class="contact contact--mail">
        <svg viewBox="0 0 28 28" aria-hidden="true"><circle cx="14" cy="14" r="12.5" fill="#fff" stroke="#c9d6ee" stroke-width="1.5"/><rect x="8.5" y="10" width="11" height="8" rx="1" fill="#1d4f9e"/><path d="M8.8 10.4 14 14.6l5.2-4.2" fill="none" stroke="#fff" stroke-width="1.1"/></svg>
        daniel@kestral.com.au
      </li>
      <li class="contact contact--web">
        <svg viewBox="0 0 28 28" aria-hidden="true"><circle cx="14" cy="14" r="12.5" fill="#fff" stroke="#c9d6ee" stroke-width="1.5"/><circle cx="14" cy="14" r="6" fill="#1d4f9e"/><path d="M8 14h12M14 8c2 2 2 10 0 12M14 8c-2 2-2 10 0 12" fill="none" stroke="#fff" stroke-width="0.9"/></svg>
        www.kestral.com
      </li>
    </ul>

    <p class="licence">Real Estate Lic: 5172936 &amp; 5172937</p>
  </section>

  <section class="card card--back" aria-label="Business card back">
    <p class="tagline">PROPERTY DEVELOPMENT &amp; SITE ACQUISITION SPECIALISTS</p>

    <div class="brand brand--back">
      <span class="brand__square"></span>
      <span class="brand__name">
        <span class="brand__word">KESTRAL</span>
        <span class="brand__sub">PROPERTY GROUP</span>
      </span>
    </div>

    <div class="offer-band">
      <p>Ask me about our <strong>INVESTMENT &amp; PARTNERSHIP</strong> opportunities</p>
    </div>
  </section>

</main>
</body>
</html>
```